Business Card and Stationary Design

After the successful redesign of our logo we are wanting to follow suite and create a new business card and stationary design!

New Logo is attached, information required on the business card should contain a mixture of the following but layout/arrangement is up to the designer.

Happy if the national provider number and abn are on the back, and happy for them to be smaller than the rest.

I am also happy to receive single sided or weird and wonderful designs.

Name
Title
National Provider Number 7291
ABN 53 219 864 317
Level 3, 42 Marlow Street
Ashcombe NSW 2291
Ph: 1300 987 214
Mobile: 0432 785 619
name@ferngatebuild.com.au
www.ferngatebuild.com.au

Target Market(s)

Professionals, Peers, Students, Suppliers...

Industry/Entity Type

Construction

Contact Information for Business Card

Listed in project description

Font styles to use
Other font styles liked:
• Century Gothic

Colors
0455a3
3176b5
ffffff

Requirements
Must have
• Professional Design, same color scheme as our logo
Nice to have
• Something that sets our apart from everyone else would be fantastic, open to size and shape and layout options, as long as they present professionally.
• Open to raised/embossed text, alternative materials, custom sizes, clear material
Should not have
• The color orange

```html
<!DOCTYPE html>
<html lang="en">
<head>
<meta charset="utf-8">
<title>Ferngate Build — Business Card</title>
<link rel="stylesheet" href="https://fonts.googleapis.com/css2?family=Questrial&display=swap">
<style>
  :root {
    --navy: #1f3a78;
    --navy-back: #1f3a7a;
    --grey-text: #6d6e71;
    --white: #ffffff;
    --page: #eceeef;
  }
  * { margin: 0; padding: 0; box-sizing: border-box; }
  html, body {
    width: 1200px; height: 1000px; overflow: hidden;
    background: var(--page);
    font-family: "Questrial", "Century Gothic", sans-serif;
  }
  .stage { position: relative; width: 1200px; height: 1000px; }

  .card {
    position: absolute; left: 240px; width: 696px; height: 396px;
    box-shadow: 0 2px 6px rgba(0,0,0,0.18);
  }
  .card--front { top: 83px; background: var(--white); }
  .card--back { top: 520px; background: var(--navy-back); }

  .holder { position: absolute; left: 30px; top: 34px; }
  .holder__name { color: var(--navy); font-size: 20px; letter-spacing: 0.5px; line-height: 1.2; }
  .holder__title { color: var(--grey-text); font-size: 16px; margin-top: 4px; }

  .brand {
    position: absolute; display: flex; align-items: center; gap: 10px;
    font-weight: 400; white-space: nowrap;
  }
  .brand__mark { display: block; }
  .card--front .brand { right: 26px; top: 28px; color: var(--navy); font-size: 32px; }
  .card--front .brand__mark { width: 18px; height: 18px; background: var(--navy); }
  .card--back .brand { left: 50%; top: 50%; transform: translate(-50%, -50%); color: var(--white); font-size: 52px; gap: 16px; }
  .card--back .brand__mark { width: 30px; height: 30px; background: var(--white); }

  .contact { position: absolute; left: 34px; top: 170px; list-style: none; }
  .contact__item {
    display: flex; align-items: center; gap: 13px;
    color: var(--grey-text); font-size: 16px; line-height: 20.5px;
  }
  .contact__icon { width: 14px; height: 14px; fill: var(--navy); flex: none; }

  .address { position: absolute; left: 31px; top: 271px; color: var(--grey-text); font-size: 16px; line-height: 21.5px; font-style: normal; }
  .registration { position: absolute; left: 31px; top: 327px; color: var(--navy); font-size: 16px; line-height: 22px; }
</style>
</head>
<body>
<main class="stage">

  <section class="card card--front" aria-label="Business card front">
    <div class="holder">
      <p class="holder__name">DANIEL CARVER</p>
      <p class="holder__title">Director</p>
    </div>

    <div class="brand"><span class="brand__mark"></span>ferngate build</div>

    <ul class="contact">
      <li class="contact__item">
        <svg class="contact__icon" viewBox="0 0 14 14" aria-hidden="true"><path d="M4 0h6a1 1 0 0 1 1 1v12a1 1 0 0 1-1 1H4a1 1 0 0 1-1-1V1a1 1 0 0 1 1-1zm0.5 2v9h5V2z"/></svg>
        0432 785 619
      </li>
      <li class="contact__item">
        <svg class="contact__icon" viewBox="0 0 14 14" aria-hidden="true"><path d="M3 1l2.2 3-1.3 1.4c.8 1.8 2.3 3.3 4.1 4.1L9.4 8.2 12.5 10.4 11.4 13C5.8 12.6 1.3 8.2 1 2.6z"/></svg>
        1300 987 214
      </li>
      <li class="contact__item">
        <svg class="contact__icon" viewBox="0 0 14 14" aria-hidden="true"><path d="M1 3h12v8H1zM1.5 3.5L7 8l5.5-4.5v1L7 9 1.5 4.5z" fill-rule="evenodd"/></svg>
        name@ferngatebuild.com.au
      </li>
      <li class="contact__item">
        <svg class="contact__icon" viewBox="0 0 14 14" aria-hidden="true"><circle cx="7" cy="7" r="6"/><path d="M3 6h8M3 8h8M7 1c-2 3-2 9 0 12M7 1c2 3 2 9 0 12" stroke="#fff" stroke-width="0.8" fill="none"/></svg>
        www.ferngatebuild.com.au
      </li>
    </ul>

    <address class="address">Level 3, 42 Marlow Street<br>Ashcombe NSW 2291</address>

    <p class="registration">ABN 53 219 864 317<br>National Provider Number 7291</p>
  </section>

  <section class="card card--back" aria-label="Business card back">
    <div class="brand"><span class="brand__mark"></span>ferngate build</div>
  </section>

</main>
</body>
</html>
```